Business card for a shipping supplies business

Needing a business card design. Please see the logo. The logo with the white font should be used if there is a dark background.

We are looking for the following info on the card. Please see the sample info. We will need the info to be changed with a few different employee names and info but all will use the same template.

Business Name: The Crate Heron
Employee Name : Marcus Delaney
Position: Account Manager
Address: 4827 W. Ridge 418 S.
Fort Worth, TX 73948
email: Marcus@thecrateheron.example
telephone: 855-619-2740 x 207
website: www.getparcelkits.example

Target Market(s)

Businesses who ship products for online sales

Industry/Entity Type

Cardboard

Contact Information for Business Card

Name, title, address, website, logo, telephone number

Font styles to use
Sans Serif

Colors
EE7325
F08F49
F5BC92
FAE3D3
FDF4ED

Requirements
Must have
• Logo on back of card. Clean look, just logo, website address

```html
<!DOCTYPE html>
<html lang="en">
<head>
<meta charset="utf-8">
<title>The Crate Heron — Business Card</title>
<link rel="stylesheet" href="https://fonts.googleapis.com/css2?family=Archivo:wght@500;800&display=swap">
<style>
  :root {
    --backdrop: #d6d0d0;
    --card-light: #fee8da;
    --card-warm: #eed3c3;
    --orange: #ee7325;
    --orange-deep: #e2571a;
    --ink: #111111;
    --divider: #2e2c45;
    --white: #ffffff;
  }
  * { margin: 0; padding: 0; box-sizing: border-box; }
  html, body {
    width: 1200px; height: 1200px; overflow: hidden;
    background: var(--backdrop);
    font-family: "Archivo", Arial, sans-serif;
  }
  .canvas { position: relative; width: 1200px; height: 1200px; }
  .card {
    position: absolute; left: 251px; width: 705px; height: 403px;
    background: linear-gradient(100deg, var(--card-light) 0%, var(--card-warm) 100%);
  }
  .card--front { top: 148px; }
  .card--back { top: 656px; }

  .brand-name {
    position: absolute; font-weight: 800; color: var(--orange-deep);
    white-space: nowrap; letter-spacing: 0.5px;
  }
  .brand-mark {
    position: absolute; background: var(--orange);
  }
  .card--front .brand-mark { left: 320px; top: 112px; width: 64px; height: 64px; }
  .card--front .brand-name { left: 0; width: 100%; text-align: center; top: 232px; font-size: 38px; }
  .front-web {
    position: absolute; left: 0; width: 100%; text-align: center; top: 288px;
    font-size: 12.5px; font-weight: 800; letter-spacing: 1.6px; color: var(--ink);
  }

  .person { position: absolute; left: 60px; top: 84px; }
  .person-name {
    font-size: 18px; font-weight: 800; letter-spacing: 1.8px; color: var(--ink);
    padding-bottom: 3px; border-bottom: 3px solid var(--orange); display: inline-block;
  }
  .person-title {
    margin-top: 7px; margin-left: 2px;
    font-size: 7px; font-weight: 800; letter-spacing: 0.6px; color: var(--ink);
  }

  .contact-list { position: absolute; left: 61px; top: 181px; list-style: none; }
  .contact-item { display: flex; align-items: flex-start; margin-bottom: 15px; }
  .contact-icon {
    width: 19px; height: 19px; background: var(--orange); flex: none;
    display: flex; align-items: center; justify-content: center;
  }
  .contact-text {
    margin-left: 16px; margin-top: 3px;
    font-size: 11px; font-weight: 800; letter-spacing: 1.6px; color: var(--ink); line-height: 20px;
    margin-top: -1px;
  }

  .divider {
    position: absolute; left: 400px; top: 36px; width: 4px; height: 334px;
    background: var(--divider);
  }
  .card--back .brand-mark { left: 506px; top: 148px; width: 52px; height: 52px; }
  .card--back .brand-name { left: 404px; width: 301px; text-align: center; top: 222px; font-size: 26px; }
</style>
</head>
<body>
<main class="canvas">

  <section class="card card--front" aria-label="Card front">
    <div class="brand-mark" aria-hidden="true"></div>
    <div class="brand-name">The Crate Heron</div>
    <div class="front-web">WWW.GETPARCELKITS.EXAMPLE</div>
  </section>

  <section class="card card--back" aria-label="Card back">
    <div class="person">
      <div class="person-name">MARCUS DELANEY</div>
      <div class="person-title">ACCOUNT MANAGER</div>
    </div>

    <ul class="contact-list">
      <li class="contact-item">
        <span class="contact-icon">
          <svg width="11" height="11" viewBox="0 0 24 24" aria-hidden="true"><path fill="#fff" d="M6.6 10.8a15 15 0 0 0 6.6 6.6l2.2-2.2c.3-.3.7-.4 1-.2 1.1.4 2.3.6 3.6.6.6 0 1 .4 1 1V20c0 .6-.4 1-1 1A17 17 0 0 1 3 4c0-.6.4-1 1-1h3.5c.6 0 1 .4 1 1 0 1.3.2 2.5.6 3.6.1.3 0 .7-.2 1z"/></svg>
        </span>
        <span class="contact-text">855-619-2740 x 207</span>
      </li>
      <li class="contact-item">
        <span class="contact-icon">
          <svg width="12" height="10" viewBox="0 0 24 18" aria-hidden="true"><rect x="1" y="1" width="22" height="16" fill="none" stroke="#fff" stroke-width="2"/><path d="M1 1l11 9 11-9" fill="none" stroke="#fff" stroke-width="2"/></svg>
        </span>
        <span class="contact-text">MARCUS@THECRATEHERON.EXAMPLE</span>
      </li>
      <li class="contact-item">
        <span class="contact-icon">
          <svg width="12" height="12" viewBox="0 0 24 24" aria-hidden="true"><circle cx="12" cy="12" r="10" fill="none" stroke="#fff" stroke-width="2"/><ellipse cx="12" cy="12" rx="4.5" ry="10" fill="none" stroke="#fff" stroke-width="2"/><path d="M2 12h20" stroke="#fff" stroke-width="2"/></svg>
        </span>
        <span class="contact-text">WWW.GETPARCELKITS.EXAMPLE</span>
      </li>
      <li class="contact-item">
        <span class="contact-icon" style="margin-top:6px">
          <svg width="10" height="12" viewBox="0 0 20 24" aria-hidden="true"><path fill="#fff" d="M10 0a8 8 0 0 0-8 8c0 6 8 16 8 16s8-10 8-16a8 8 0 0 0-8-8zm0 11a3 3 0 1 1 0-6 3 3 0 0 1 0 6z"/></svg>
        </span>
        <span class="contact-text">4827 W. RIDGE 418 S.<br>FORT WORTH, TX 73948</span>
      </li>
    </ul>

    <div class="divider" aria-hidden="true"></div>

    <div class="brand-mark" aria-hidden="true"></div>
    <div class="brand-name">The Crate Heron</div>
  </section>

</main>
</body>
</html>
```